web page look and feel - B2B enterprise application

We have an enterprise application with 10 to 15 core pages and several supporting pages or popups. To start, we want the graphical design of the Users, Roles and Data Source pages and their supporting popups, wizards, etc. to be made beautiful. That is around 10 pages in total. There is a fair amount of redundancy among the pages. I have attached 5 screenshots. We very much want the pages to project a premium feel. That is absolutely essential. The color scheme is blue and sometimes yellow (only if it makes the page look better) plus black, gray and white. If the design of these screens goes well, we would expand the project to continue with other pages. The core of what we are looking for is graphic in nature but we are open to workflow suggestions if you have them. The Roles screen needs some improvements to the layout. I am looking for everything that includes icons, fonts, spacing, etc. I assume getting to the final design will take some back and forth with multiple revisions.

Target Market(s)

Large Enterprises

Number of Pages Required

5+ page

Requirements
Must have
• Premium feel

```html
<!DOCTYPE html>
<html lang="en">
<head>
<meta charset="utf-8">
<title>Norvale Data – Admin Screens</title>
<link href="https://fonts.googleapis.com/css2?family=Lato:wght@400;700;900&display=swap" rel="stylesheet">
<style>
:root{
  --stage:#d8d8d8;
  --topbar:#1b1b1b;
  --sidebar:#252b40;
  --sidebar-sub:#1b2032;
  --content:#eeeff1;
  --panel:#ffffff;
  --head:#262c42;
  --row:#f4f4f5;
  --row-alt:#e9e9ea;
  --line:#d3d4d8;
  --ink:#222;
  --muted:#555;
  --blue:#2d6cb4;
  --accent:#f2b418;
}
*{box-sizing:border-box;margin:0;padding:0}
html,body{width:931px;height:1200px;overflow:hidden}
body{background:var(--stage);font-family:"Lato",sans-serif;color:var(--ink);position:relative}
svg.defs{position:absolute;width:0;height:0}
.screen{position:absolute;background:var(--content);overflow:hidden}
.screen--users{left:94px;top:30px;width:744px;height:401px}
.screen--sources{left:94px;top:458px;width:744px;height:416px}
.screen--roles{left:19px;top:903px;width:893px;height:265px}
.topbar{height:37px;background:var(--topbar);display:flex;align-items:center;padding:0 8px;color:#fff}
.brand{display:flex;align-items:center;gap:5px;font-size:11px;font-weight:700;letter-spacing:.1px;width:110px}
.brand-dot{width:9px;height:9px;border-radius:50%;background:var(--accent)}
.menu-toggle{width:15px;height:15px;border-radius:50%;background:#555;display:flex;align-items:center;justify-content:center;margin-left:10px}
.topbar-tools{margin-left:auto;display:flex;align-items:center;gap:8px}
.topbar-tools svg{width:11px;height:11px;fill:#fff}
.user-menu{font-size:5.5px;margin-left:4px}
.layout{display:flex;height:calc(100% - 37px)}
.sidebar{width:127px;background:var(--sidebar);color:#fff;padding-top:5px;flex:none}
.nav-item{display:flex;align-items:center;gap:5px;height:22px;padding-left:8px;font-size:6.4px;font-weight:700;letter-spacing:.2px}
.nav-item svg{width:6px;height:6px;fill:#fff}
.nav-sub{background:var(--sidebar-sub);padding:1px 0}
.nav-sub div{height:15px;line-height:15px;padding-left:19px;font-size:5.8px;color:#e4e6ee;border-top:1px solid #2c3248}
.nav-sub div:first-child{border-top:0}
.main{flex:1;padding:0 7px;position:relative}
.page-head{display:flex;align-items:center;height:36px}
.page-title{font-size:15px;font-weight:900;color:var(--head)}
.add-btn{margin-left:6px;font-size:5px;background:#fff;border:1px solid #ccc;border-radius:2px;padding:1px 4px;display:flex;align-items:center;gap:2px}
.add-btn i{width:5px;height:5px;border-radius:50%;background:#333;display:inline-block}
.search{margin-left:auto;display:flex;align-items:center;gap:4px;font-size:4.5px;color:#777}
.search-box{width:110px;height:10px;background:#fff;border:1px solid #d5d5d5;border-radius:1px;display:flex;align-items:center;justify-content:space-between;padding:0 3px}
.search-box svg{width:6px;height:6px}
.panel{background:var(--panel);padding-bottom:6px}
.row{display:grid;align-items:center;font-size:6.3px;height:21px}
.row>span{padding-left:7px;height:100%;display:flex;align-items:center;border-right:1px solid var(--line)}
.row>span:last-child{border-right:0}
.row--head{background:var(--head);color:#fff;font-size:6.8px}
.row--head>span{border-right:1px solid #40465c}
.row--body{background:var(--row);border-bottom:4px solid #fff}
.toggle svg{width:7px;height:7px;fill:none;stroke:#333;stroke-width:2}
.actions{gap:7px;justify-content:center;padding-left:0 !important}
.actions svg{width:7px;height:7px;fill:var(--blue)}
.users-grid{grid-template-columns:30px 96px 96px 105px 152px 67px 56px}
.detail{padding:2px 0 8px;border-bottom:6px solid var(--content);margin-bottom:6px}
.detail-row{display:grid;grid-template-columns:327px 220px 56px;height:19px;align-items:center;font-size:6.1px}
.detail-row>span{padding-left:11px;display:flex;align-items:center;gap:4px;height:100%}
.detail-row>span:nth-child(2){border-left:1px solid var(--line);padding-left:9px}
.detail-row .actions{justify-content:flex-end;padding-right:30px}
.detail-row--odd{background:#ececed}
.detail-row--even{background:#e2e2e4}
.cb{width:5px;height:5px;border:1px solid #999;background:#fff;display:inline-flex;align-items:center;justify-content:center;flex:none}
.cb.on::after{content:"";width:2px;height:3px;border:solid #333;border-width:0 1px 1px 0;transform:rotate(45deg) translate(0,-.5px)}
.perm{display:inline-flex;align-items:center;gap:2px;margin-right:8px}
.pager{display:flex;justify-content:center;align-items:center;gap:9px;height:22px;margin-top:6px}
.pager svg{width:7px;height:6px;fill:#777}
.page-no{width:12px;height:12px;border-radius:50%;background:var(--blue);color:#fff;font-size:6px;display:flex;align-items:center;justify-content:center}
.page-size{width:25px;height:9px;border:1px solid #ccc;font-size:4.5px;display:flex;align-items:center;justify-content:space-between;padding:0 3px;margin-left:4px}
.copyright{text-align:center;font-size:5px;color:#333;position:absolute;left:0;right:0}
.sources-grid{grid-template-columns:30px 192px 175px 164px 41px}
.objects{margin:0 4px;background:#eee;padding:0 0 6px 26px;border-left:1px solid var(--line);position:relative}
.objects-inner{border-left:1px solid #ccc;background:#fff}
.objects-title{height:22px;display:flex;align-items:center;justify-content:center;font-size:6.4px;position:relative;background:#fff}
.pill{position:absolute;right:10px;font-size:4.6px;border:1px solid #ccc;border-radius:2px;padding:1px 3px;display:flex;align-items:center;gap:2px;background:#fff}
.pill i{width:4px;height:4px;border-radius:50%;background:#333}
.obj-grid{grid-template-columns:22px 473px 50px 26px}
.obj-grid.row{height:19px;font-size:6.2px;border-bottom:1px solid #e3e3e3}
.fields{margin-left:22px;background:#efefef}
.fields-head{height:22px;background:#d9d9da;display:flex;align-items:center;padding-left:9px;font-size:6.4px;position:relative}
.field-grid{grid-template-columns:154px 171px 68px 126px 26px;padding-left:6px}
.field-grid.row{height:21px;font-size:5.2px}
.field-grid.row--th{height:18px;font-size:5px;background:#fff}
.field-grid.row--field{background:#fff;border-bottom:1px solid #ececec}
.field-grid .center{justify-content:center;padding-left:0}
.rule-icons{gap:13px;justify-content:flex-start}
.rule-icons svg{width:6px;height:6px;fill:none;stroke:var(--blue);stroke-width:1.6}
.roles-grid{grid-template-columns:74px 71px 74px 71px 70px 78px 90px 108px 63px 51px}
.roles-grid.row--body{height:24px;font-size:5.1px;background:#f2f2f3}
.roles-grid.row--body>span{gap:0;border-right:1px solid #e0e0e0}
.roles-grid .actions{justify-content:flex-start;padding-left:7px !important}
</style>
</head>
<body>
<svg class="defs" aria-hidden="true">
  <symbol id="i-edit" viewBox="0 0 12 12"><path d="M1 3h5v1H2v6h6V6h1v5H1z"/><path d="M9 1l2 2-5 5H4V6z"/></symbol>
  <symbol id="i-copy" viewBox="0 0 12 12"><path d="M4 1h7v7H4zM5 2v5h5V2z"/><path d="M1 4h2v1H2v5h5V9h1v2H1z"/></symbol>
  <symbol id="i-trash" viewBox="0 0 12 12"><path d="M2 2h8v1.5H2zM5 1h2v1H5z"/><path d="M3 4h6l-.5 7h-5z"/></symbol>
  <symbol id="i-down" viewBox="0 0 10 10"><path d="M2 3.5l3 3 3-3"/></symbol>
  <symbol id="i-right" viewBox="0 0 10 10"><path d="M3.5 2l3 3-3 3"/></symbol>
  <symbol id="i-first" viewBox="0 0 10 8"><path d="M1 0h1v8H1zM10 0v8L6 4zM6 0v8L2 4z"/></symbol>
  <symbol id="i-prev" viewBox="0 0 10 8"><path d="M9 0v8L5 4zM5 0v8L1 4z"/></symbol>
  <symbol id="i-next" viewBox="0 0 10 8"><path d="M1 0v8l4-4zM5 0v8l4-4z"/></symbol>
  <symbol id="i-last" viewBox="0 0 10 8"><path d="M0 0v8l4-4zM4 0v8l4-4zM8 0h1v8H8z"/></symbol>
  <symbol id="i-search" viewBox="0 0 10 10"><circle cx="4" cy="4" r="3" fill="none" stroke="#333" stroke-width="1.5"/><path d="M6 6l3 3" stroke="#333" stroke-width="1.5"/></symbol>
  <symbol id="i-gauge" viewBox="0 0 12 12"><path d="M6 1a5.5 5.5 0 0 0-5.5 5.5c0 1.5.6 2.9 1.6 3.9h7.8a5.5 5.5 0 0 0-3.9-9.4zm0 7a1 1 0 0 1-.8-1.6L8 3.5 6.9 7.4A1 1 0 0 1 6 8z"/></symbol>
  <symbol id="i-wand" viewBox="0 0 12 12"><path d="M1 10l7-7 1 1-7 7zM9 0l.5 1.5L11 2l-1.5.5L9 4l-.5-1.5L7 2l1.5-.5z"/></symbol>
  <symbol id="i-help" viewBox="0 0 12 12"><path d="M6 0a6 6 0 1 0 0 12A6 6 0 0 0 6 0zm.7 9.5H5.3V8.2h1.4zm1.2-4.4c-.4.6-1.2.9-1.2 1.7v.3H5.3v-.4c0-1.3 1.3-1.5 1.3-2.3 0-.4-.3-.7-.7-.7s-.8.3-.8.9H3.7c0-1.3 1-2.1 2.2-2.1 1.3 0 2.2.8 2.2 1.8 0 .3-.1.6-.2.8z"/></symbol>
  <symbol id="i-gear" viewBox="0 0 12 12"><path d="M5 0h2l.3 1.6 1.2.6 1.4-.9 1.4 1.4-.9 1.4.6 1.2L12 5v2l-1.6.3-.6 1.2.9 1.4-1.4 1.4-1.4-.9-1.2.6L7 12H5l-.3-1.6-1.2-.6-1.4.9-1.4-1.4.9-1.4-.6-1.2L0 7V5l1.6-.3.6-1.2-.9-1.4 1.4-1.4 1.4.9 1.2-.6zm1 4a2 2 0 1 0 0 4 2 2 0 0 0 0-4z"/></symbol>
  <symbol id="i-users" viewBox="0 0 12 12"><circle cx="4" cy="3.5" r="2"/><circle cx="8.5" cy="4" r="1.6"/><path d="M0 10c0-2.5 1.8-4 4-4s4 1.5 4 4zM8 10c0-1.5-.4-2.6-1-3.4 2.5-.6 5 .5 5 3.4z"/></symbol>
  <symbol id="i-db" viewBox="0 0 12 12"><ellipse cx="6" cy="2" rx="5" ry="1.6"/><path d="M1 4c2 1.6 8 1.6 10 0v2c-2 1.6-8 1.6-10 0zM1 8c2 1.6 8 1.6 10 0v2c-2 1.6-8 1.6-10 0z"/></symbol>
  <symbol id="i-link" viewBox="0 0 12 12"><path d="M0 5h6V2l5 4-5 4V7H0z"/></symbol>
  <symbol id="i-grid" viewBox="0 0 12 12"><path d="M0 0h3v3H0zM4.5 0h3v3h-3zM9 0h3v3H9zM0 4.5h3v3H0zM4.5 4.5h3v3h-3zM9 4.5h3v3H9zM0 9h3v3H0zM4.5 9h3v3h-3zM9 9h3v3H9z"/></symbol>
  <symbol id="i-list" viewBox="0 0 12 12"><path d="M0 1h12v2H0zM2 5h10v2H2zM0 9h12v2H0z"/></symbol>
  <symbol id="i-clock" viewBox="0 0 12 12"><path d="M6 0a6 6 0 1 0 0 12A6 6 0 0 0 6 0zm0 2a4 4 0 1 1 0 8 4 4 0 0 1 0-8zm-.6 1v3.3l2.4 1.5.6-.9-1.8-1.1V3z"/></symbol>
  <symbol id="i-sync" viewBox="0 0 12 12"><path d="M6 1a5 5 0 0 1 4.5 2.8L12 2v4H8l1.4-1.4A3.5 3.5 0 0 0 2.6 5H1A5 5 0 0 1 6 1zM0 6h4L2.6 7.4A3.5 3.5 0 0 0 9.4 7H11a5 5 0 0 1-9.5 1.2L0 10z"/></symbol>
  <symbol id="r-text" viewBox="0 0 10 10"><path d="M1 8c0-2 3-2 3-4s-3-1-3 0M4 8V4M6 6l1.5 1.5L10 2"/></symbol>
  <symbol id="r-undo" viewBox="0 0 10 10"><path d="M2 3a4 4 0 1 1 0 4M2 1v2h2"/></symbol>
  <symbol id="r-edit" viewBox="0 0 10 10"><path d="M1 2h4M1 2v7h7V5M4 6l5-5"/></symbol>
  <symbol id="r-tree" viewBox="0 0 10 10"><path d="M0 5h5M5 5l4-3M5 5l4 3M5 5h4"/></symbol>
  <symbol id="r-dot" viewBox="0 0 10 10"><circle cx="5" cy="5" r="3.5"/><circle cx="5" cy="5" r="1.2"/></symbol>
  <symbol id="r-lines" viewBox="0 0 10 10"><path d="M0 2h10M3 5h7M0 8h10M0 5h1"/></symbol>
</svg>

<!-- Users screen -->
<section class="screen screen--users">
  <header class="topbar">
    <div class="brand"><span class="brand-dot"></span>Norvale Data</div>
    <div class="menu-toggle"><svg width="7" height="7" viewBox="0 0 10 10" fill="#fff"><path d="M1 2h8v1.4H1zM1 4.3h8v1.4H1zM1 6.6h8V8H1z"/></svg></div>
    <div class="topbar-tools">
      <svg><use href="#i-gauge"/></svg><svg><use href="#i-wand"/></svg><svg><use href="#i-help"/></svg><svg><use href="#i-gear"/></svg>
      <span class="user-menu">Hal Harbor ⌄</span>
    </div>
  </header>
  <div class="layout">
    <nav class="sidebar">
      <div class="nav-item"><svg><use href="#i-users"/></svg>USERS</div>
      <div class="nav-sub"><div>Roles</div><div>Notification Groups</div></div>
      <div class="nav-item"><svg><use href="#i-db"/></svg>DATA SOURCES</div>
      <div class="nav-item"><svg><use href="#i-link"/></svg>DATA OBJECT RELATIONSHIPS</div>
      <div class="nav-item"><svg><use href="#i-grid"/></svg>DATA SETS</div>
      <div class="nav-item"><svg><use href="#i-list"/></svg>RULE SETS</div>
      <div class="nav-item"><svg><use href="#i-clock"/></svg>SCHEDULES</div>
      <div class="nav-item"><svg><use href="#i-sync"/></svg>METADATA IMPORT/EXPORT</div>
      <div class="nav-sub"><div>Import</div><div>Export</div></div>
    </nav>
    <main class="main">
      <div class="page-head">
        <h1 class="page-title">Users</h1>
        <span class="add-btn"><i></i>Add</span>
        <div class="search"><div class="search-box">Search<svg><use href="#i-search"/></svg></div>Advanced Search</div>
      </div>
      <div class="panel">
        <div class="row row--head users-grid">
          <span></span><span>First Name ▾</span><span>Last Name ⇕</span><span>Username ⇕</span><span>Email Address ⇕</span><span>Status ⇕</span><span></span>
        </div>
        <div class="row row--body users-grid" style="margin-top:4px">
          <span class="toggle"><svg><use href="#i-down"/></svg></span><span>tim</span><span>tim</span><span>tim.timtim</span><span>tim@norvale.io</span><span>Active</span>
          <span class="actions"><svg><use href="#i-edit"/></svg><svg><use href="#i-copy"/></svg><svg><use href="#i-trash"/></svg></span>
        </div>
        <div class="detail">
          <div class="detail-row"><span>Object</span><span>Permissions</span><span class="actions"><svg><use href="#i-edit"/></svg></span></div>
          <div class="detail-row detail-row--odd"><span>System Settings</span><span><span class="perm"><i class="cb on"></i>Read</span><span class="perm"><i class="cb on"></i>Write</span></span><span class="actions"><svg><use href="#i-edit"/></svg></span></div>
          <div class="detail-row detail-row--even"><span>Users</span><span><span class="perm"><i class="cb on"></i>Read</span><span class="perm"><i class="cb on"></i>Write</span></span><span class="actions"><svg><use href="#i-edit"/></svg></span></div>
          <div class="detail-row detail-row--odd"><span>Data Source</span><span>Role</span><span class="actions"><svg><use href="#i-edit"/></svg></span></div>
          <div class="detail-row detail-row--even"><span>All Data Sources</span><span>System Administrator</span><span class="actions"><svg><use href="#i-edit"/></svg></span></div>
        </div>
        <div class="row row--body users-grid"><span class="toggle"><svg><use href="#i-down"/></svg></span><span>Test</span><span>User</span><span>test.user</span><span>tim.renwick999@mailpost.com</span><span>Active</span><span class="actions"><svg><use href="#i-edit"/></svg><svg><use href="#i-copy"/></svg><svg><use href="#i-trash"/></svg></span></div>
        <div class="row row--body users-grid"><span class="toggle"><svg><use href="#i-down"/></svg></span><span>test</span><span>test</span><span>testtesttest</span><span>test@test.com</span><span>Active</span><span class="actions"><svg><use href="#i-edit"/></svg><svg><use href="#i-copy"/></svg><svg><use href="#i-trash"/></svg></span></div>
        <div class="row row--body users-grid"><span class="toggle"><svg><use href="#i-down"/></svg></span><span>sam</span><span>spruce</span><span>sam.spruce2</span><span>sam@norvale.io</span><span>Inactive</span><span class="actions"><svg><use href="#i-edit"/></svg><svg><use href="#i-copy"/></svg><svg><use href="#i-trash"/></svg></span></div>
        <div class="row row--body users-grid"><span class="toggle"><svg><use href="#i-down"/></svg></span><span>Hal</span><span>Harbor</span><span>harbor.test</span><span>tom.renwick@norvale.io</span><span>Active</span><span class="actions"><svg><use href="#i-edit"/></svg><svg><use href="#i-copy"/></svg><svg><use href="#i-trash"/></svg></span></div>
        <div class="row row--body users-grid"><span class="toggle"><svg><use href="#i-down"/></svg></span><span>bo</span><span>barlow</span><span>bo.barlow</span><span>bo@mailpost.com</span><span>Active</span><span class="actions"><svg><use href="#i-edit"/></svg><svg><use href="#i-copy"/></svg><svg><use href="#i-trash"/></svg></span></div>
        <div class="pager"><svg><use href="#i-first"/></svg><svg><use href="#i-prev"/></svg><span class="page-no">1</span><svg><use href="#i-next"/></svg><svg><use href="#i-last"/></svg><span class="page-size">20<span>▾</span></span></div>
      </div>
      <p class="copyright" style="top:379px">Copyright © 2018 Norvale Data. &nbsp;All rights reserved.</p>
    </main>
  </div>
</section>

<!-- Data Sources screen -->
<section class="screen screen--sources">
  <header class="topbar">
    <div class="brand"><span class="brand-dot"></span>Norvale Data</div>
    <div class="menu-toggle"><svg width="7" height="7" viewBox="0 0 10 10" fill="#fff"><path d="M1 2h8v1.4H1zM1 4.3h8v1.4H1zM1 6.6h8V8H1z"/></svg></div>
    <div class="topbar-tools">
      <svg><use href="#i-gauge"/></svg><svg><use href="#i-wand"/></svg><svg><use href="#i-help"/></svg><svg><use href="#i-gear"/></svg>
      <span class="user-menu">Hal Harbor ⌄</span>
    </div>
  </header>
  <div class="layout">
    <nav class="sidebar">
      <div class="nav-item"><svg><use href="#i-users"/></svg>USERS</div>
      <div class="nav-sub"><div>Roles</div><div>Notification Groups</div></div>
      <div class="nav-item"><svg><use href="#i-db"/></svg>DATA SOURCES</div>
      <div class="nav-item"><svg><use href="#i-link"/></svg>DATA OBJECT RELATIONSHIPS</div>
      <div class="nav-item"><svg><use href="#i-grid"/></svg>DATA SETS</div>
      <div class="nav-item"><svg><use href="#i-list"/></svg>RULE SETS</div>
      <div class="nav-item"><svg><use href="#i-clock"/></svg>SCHEDULES</div>
      <div class="nav-item"><svg><use href="#i-sync"/></svg>METADATA IMPORT/EXPORT</div>
      <div class="nav-sub"><div>Import</div><div>Export</div></div>
    </nav>
    <main class="main">
      <div class="page-head">
        <h1 class="page-title">Data Sources</h1>
        <span class="add-btn"><i></i>Add</span>
        <div class="search"><div class="search-box">Search<svg><use href="#i-search"/></svg></div>Advanced Search</div>
      </div>
      <div class="panel">
        <div class="row row--head sources-grid"><span></span><span>Data Source Name ▴</span><span>Type ⇕</span><span>Status ⇕</span><span></span></div>
        <div class="row row--body sources-grid" style="margin-top:4px"><span class="toggle"><svg><use href="#i-right"/></svg></span><span>RelayDB</span><span></span><span>Active</span><span class="actions"><svg><use href="#i-edit"/></svg><svg><use href="#i-trash"/></svg></span></div>
        <div class="row row--body sources-grid"><span class="toggle"><svg><use href="#i-down"/></svg></span><span>CLCRM</span><span>Cloudline CRM</span><span>Active</span><span class="actions"><svg><use href="#i-edit"/></svg><svg><use href="#i-trash"/></svg></span></div>
        <div class="objects">
          <div class="objects-inner">
            <div class="objects-title">Data Objects<span class="pill"><i></i>Add Data Objects</span></div>
            <div class="row obj-grid"><span></span><span style="justify-content:center;padding-left:0">Name</span><span></span><span></span></div>
            <div class="row obj-grid"><span class="toggle"><svg><use href="#i-down"/></svg></span><span>Account</span><span>19 fields</span><span class="actions"><svg><use href="#i-trash"/></svg></span></div>
            <div class="fields">
              <div class="fields-head">Fields<span class="pill"><i></i>Add Fields</span></div>
              <div class="row row--th field-grid"><span>Field Name</span><span>Data Type</span><span>Primary Key</span><span>Rule Types</span><span></span></div>
              <div class="row row--field field-grid"><span>Account Fax</span><span></span><span class="center"><i class="cb"></i></span><span class="rule-icons"><svg><use href="#r-text"/></svg><svg><use href="#r-undo"/></svg><svg><use href="#r-edit"/></svg><svg><use href="#r-tree"/></svg><svg><use href="#r-dot"/></svg><svg><use href="#r-lines"/></svg></span><span class="actions"><svg><use href="#i-edit"/></svg><svg><use href="#i-trash"/></svg></span></div>
              <div class="row row--field field-grid"><span>Account ID</span><span>Addres Line 1</span><span class="center"><i class="cb on"></i></span><span class="rule-icons"><svg><use href="#r-text"/></svg><svg><use href="#r-undo"/></svg><svg><use href="#r-edit"/></svg><svg><use href="#r-tree"/></svg><svg><use href="#r-dot"/></svg><svg><use href="#r-lines"/></svg></span><span class="actions"><svg><use href="#i-edit"/></svg><svg><use href="#i-trash"/></svg></span></div>
              <div class="row row--field field-grid"><span>Account Name</span><span></span><span class="center"><i class="cb"></i></span><span class="rule-icons"><svg><use href="#r-text"/></svg><svg><use href="#r-undo"/></svg><svg><use href="#r-edit"/></svg><svg><use href="#r-tree"/></svg><svg><use href="#r-dot"/></svg><svg><use href="#r-lines"/></svg></span><span class="actions"><svg><use href="#i-edit"/></svg><svg><use href="#i-trash"/></svg></span></div>
              <div class="row row--field field-grid"><span>Billing City</span><span></span><span class="center"><i class="cb"></i></span><span class="rule-icons"><svg><use href="#r-text"/></svg><svg><use href="#r-undo"/></svg><svg><use href="#r-edit"/></svg><svg><use href="#r-tree"/></svg><svg><use href="#r-dot"/></svg><svg><use href="#r-lines"/></svg></span><span class="actions"><svg><use href="#i-edit"/></svg><svg><use href="#i-trash"/></svg></span></div>
              <div class="row row--field field-grid"><span>Billing Country</span><span></span><span class="center"><i class="cb"></i></span><span class="rule-icons"><svg><use href="#r-text"/></svg><svg><use href="#r-undo"/></svg><svg><use href="#r-edit"/></svg><svg><use href="#r-tree"/></svg><svg><use href="#r-dot"/></svg><svg><use href="#r-lines"/></svg></span><span class="actions"><svg><use href="#i-edit"/></svg><svg><use href="#i-trash"/></svg></span></div>
              <div style="height:14px"></div>
            </div>
          </div>
        </div>
      </div>
      <p class="copyright" style="top:398px">Copyright © 2018 Norvale Data. &nbsp;All rights reserved.</p>
    </main>
  </div>
</section>

<!-- Roles screen -->
<section class="screen screen--roles">
  <header class="topbar">
    <div class="brand"><span class="brand-dot"></span>Norvale Data</div>
    <div class="menu-toggle"><svg width="7" height="7" viewBox="0 0 10 10" fill="#fff"><path d="M1 2h8v1.4H1zM1 4.3h8v1.4H1zM1 6.6h8V8H1z"/></svg></div>
    <div class="topbar-tools">
      <svg><use href="#i-gauge"/></svg><svg><use href="#i-wand"/></svg><svg><use href="#i-help"/></svg><svg><use href="#i-gear"/></svg>
      <span class="user-menu">Hal Harbor ⌄</span>
    </div>
  </header>
  <div class="layout">
    <nav class="sidebar">
      <div class="nav-item"><svg><use href="#i-users"/></svg>USERS</div>
      <div class="nav-sub"><div>Roles</div><div>Notification Groups</div></div>
      <div class="nav-item"><svg><use href="#i-db"/></svg>DATA SOURCES</div>
      <div class="nav-item"><svg><use href="#i-link"/></svg>DATA OBJECT RELATIONSHIPS</div>
      <div class="nav-item"><svg><use href="#i-grid"/></svg>DATA SETS</div>
      <div class="nav-item"><svg><use href="#i-list"/></svg>RULE SETS</div>
      <div class="nav-item"><svg><use href="#i-clock"/></svg>SCHEDULES</div>
      <div class="nav-item"><svg><use href="#i-sync"/></svg>METADATA IMPORT/EXPORT</div>
      <div class="nav-sub"><div>Import</div><div>Export</div></div>
    </nav>
    <main class="main">
      <div class="page-head">
        <h1 class="page-title">Roles</h1>
        <span class="add-btn"><i></i>Add</span>
        <div class="search"><div class="search-box" style="width:105px">Search<svg><use href="#i-search"/></svg></div>Advanced Search</div>
      </div>
      <div class="panel">
        <div class="row row--head roles-grid"><span>Role Name ▾</span><span>Data Sources</span><span>Data Sets</span><span>Rule Sets</span><span>Schedules</span><span>Suspect Matches</span><span>Master Data Objects</span><span>Metadata Import / Export</span><span>API</span><span></span></div>
        <div class="row row--body roles-grid" style="margin-top:4px"><span>System Administrator</span>
          <span><span class="perm"><i class="cb on"></i>Read</span><span class="perm"><i class="cb on"></i>Write</span></span>
          <span><span class="perm"><i class="cb on"></i>Read</span><span class="perm"><i class="cb on"></i>Write</span></span>
          <span><span class="perm"><i class="cb on"></i>Read</span><span class="perm"><i class="cb on"></i>Write</span></span>
          <span><span class="perm"><i class="cb on"></i>Read</span><span class="perm"><i class="cb on"></i>Write</span></span>
          <span><span class="perm"><i class="cb on"></i>Read</span><span class="perm"><i class="cb on"></i>Write</span></span>
          <span><span class="perm"><i class="cb on"></i>Read</span><span class="perm"><i class="cb on"></i>Write</span></span>
          <span><span class="perm"><i class="cb on"></i>Read</span><span class="perm"><i class="cb on"></i>Write</span></span>
          <span><span class="perm"><i class="cb on"></i>Read</span><span class="perm"><i class="cb on"></i>Write</span></span>
          <span class="actions"><svg><use href="#i-edit"/></svg></span></div>
        <div class="row row--body roles-grid"><span>Role#1</span>
          <span><span class="perm"><i class="cb"></i>Read</span><span class="perm"><i class="cb"></i>Write</span></span>
          <span><span class="perm"><i class="cb on"></i>Read</span><span class="perm"><i class="cb on"></i>Write</span></span>
          <span><span class="perm"><i class="cb on"></i>Read</span><span class="perm"><i class="cb on"></i>Write</span></span>
          <span><span class="perm"><i class="cb on"></i>Read</span><span class="perm"><i class="cb on"></i>Write</span></span>
          <span><span class="perm"><i class="cb on"></i>Read</span><span class="perm"><i class="cb on"></i>Write</span></span>
          <span><span class="perm"><i class="cb on"></i>Read</span><span class="perm"><i class="cb on"></i>Write</span></span>
          <span><span class="perm"><i class="cb on"></i>Read</span><span class="perm"><i class="cb on"></i>Write</span></span>
          <span><span class="perm"><i class="cb on"></i>Read</span><span class="perm"><i class="cb on"></i>Write</span></span>
          <span class="actions"><svg><use href="#i-edit"/></svg></span></div>
        <div class="row row--body roles-grid"><span>Read Only</span>
          <span><span class="perm"><i class="cb on"></i>Read</span><span class="perm"><i class="cb"></i>Write</span></span>
          <span><span class="perm"><i class="cb on"></i>Read</span><span class="perm"><i class="cb"></i>Write</span></span>
          <span><span class="perm"><i class="cb on"></i>Read</span><span class="perm"><i class="cb"></i>Write</span></span>
          <span><span class="perm"><i class="cb on"></i>Read</span><span class="perm"><i class="cb"></i>Write</span></span>
          <span><span class="perm"><i class="cb on"></i>Read</span><span class="perm"><i class="cb"></i>Write</span></span>
          <span><span class="perm"><i class="cb on"></i>Read</span><span class="perm"><i class="cb"></i>Write</span></span>
          <span><span class="perm"><i class="cb on"></i>Read</span><span class="perm"><i class="cb"></i>Write</span></span>
          <span><span class="perm"><i class="cb on"></i>Read</span><span class="perm"><i class="cb"></i>Write</span></span>
          <span class="actions"><svg><use href="#i-edit"/></svg><svg><use href="#i-copy"/></svg><svg><use href="#i-trash"/></svg></span></div>
        <div class="row row--body roles-grid"><span>Data Administrator</span>
          <span><span class="perm"><i class="cb"></i>Read</span><span class="perm"><i class="cb"></i>Write</span></span>
          <span><span class="perm"><i class="cb"></i>Read</span><span class="perm"><i class="cb"></i>Write</span></span>
          <span><span class="perm"><i class="cb"></i>Read</span><span class="perm"><i class="cb"></i>Write</span></span>
          <span><span class="perm"><i class="cb on"></i>Read</span><span class="perm"><i class="cb on"></i>Write</span></span>
          <span><span class="perm"><i class="cb on"></i>Read</span><span class="perm"><i class="cb on"></i>Write</span></span>
          <span><span class="perm"><i class="cb"></i>Read</span><span class="perm"><i class="cb"></i>Write</span></span>
          <span><span class="perm"><i class="cb"></i>Read</span><span class="perm"><i class="cb"></i>Write</span></span>
          <span><span class="perm"><i class="cb"></i>Read</span><span class="perm"><i class="cb"></i>Write</span></span>
          <span class="actions"><svg><use href="#i-edit"/></svg></span></div>
        <div class="pager" style="margin-top:0"><svg><use href="#i-first"/></svg><svg><use href="#i-prev"/></svg><span class="page-no">1</span><svg><use href="#i-next"/></svg><svg><use href="#i-last"/></svg><span class="page-size">10<span>▾</span></span></div>
      </div>
      <p class="copyright" style="top:211px">Copyright © 2018 Norvale Data. &nbsp;All rights reserved.</p>
    </main>
  </div>
</section>
</body>
</html>
```